New Book and ebook Cover Design healing holistic/integrative cancer Project

Creation of an Ebook + Book format A5. about cure of Cancer.

Guide d'aide à la guérison

Under title Développez vos capacités de "guérisseur intérieur"
Créez votre résiliance, transmutez votre maladie en cadeaux de la vie.
Develop your self healer skills: Create your resilience, transmute your illness into gifts of life.

The 3 mains idea for the book:
- A symbolic with the icone pink of cancer with french word around (like: amour, aide, guérison, holistique, âme, corps, esprit, divin, vie):
The main target is people with cancer
Image of cancer icon ot with a tree;
- Create a Healing Journey ( image included or another idea)
- A tranversal integrative (global health soul body spirit )Journey Trough :
Spirituality, the psychoemotionnel understanding of the disease, the benefits of row ecologic foods, the medecines of the word, (Ayurveda, Chinese, Shamanism), quantum medicine, energy healing,+16 auto techniques self care
So you can illustrate the main parcours with image or icon about it
readers must feel the love the main what this book can bring them as gifts

Additionnal icon :
l’icône Verdala Pledge blue can be added. Engagement Verdala

Target Market(s)

people with cancer, professionnel of healing in integrative issue

Industry/Entity Type

Health And Wellness

Font styles to use
Other font styles liked:
• arial colibri

Colors
abd037
e667a6
a64599

Requirements
Must have
• The 3 mains idea for the book:
• - A symbolic with the icone pink of cancer with french word around (like: amour, aide, guérison, holistique, âme, corps, esprit, divin, vie):
• The main target is people with cancer
• Image of cancer icon ot with a tree;
• - Create a Healing Journey ( image included or another idea)
• - A tranversal integrative (global health soul body spirit )Journey Trough :
• Spirituality, the psychoemotionnel understanding of the disease, the benefits of row ecologic foods, the medecines of the word, (Ayurveda, Chinese, Shamanism), quantum medicine, energy healing,+16 auto techniques self care
• So you can illustrate the main parcours with image or icon about it
• readers must feel the love the main what this book can bring them as gifts
• If you don't put icone or image for the benefits about the book:
• cloud of words in cancer symbol (and replace love words by this list)
• Parcours de Guérisons : Create a Healing Journey
• Médecine Intégrative -Santé Intégrative (âme-corps-esprit) (Soul-Body-Spirit)
• Médecine du Monde (Ayurveda, Médecine Chinoise, Chamanisme) ( Ayurveda, Chinese Médicine, Shamanism)
• Alimentation vibrante ( vibrant raw food)
• Energies de guérison
• Plus de 20 Techniques d’auto-soins
Nice to have
• 1/idea of ​​backgrounds with orbs in violet color (the fine notion of connection to the universe to the divine is to be passed on in this book)
• 2/ People can Create their own Healing Journey '( image for healing journey with roads for exemple)
• 3/ cancer symbole with words around spirit of the book french word around (like: amour, aide, guérison, holistique, âme, corps, esprit, divin, vie):
• pink/magenta and green color
• 4/ idea of gift with love?
• 5/ Lucien Marvaud ( Name of autor)
• The goal is you can live, it's possible!
Should not have
• put to much information keep focuse on the spirit of the book. People in less 30 second will be interest for buy and USED this book
• use the same type of the same type of font

```html
<!DOCTYPE html>
<html lang="fr">
<head>
<meta charset="utf-8">
<title>Quatrième de couverture – Guide d'aide à la guérison</title>
<link rel="preconnect" href="https://fonts.googleapis.com">
<link href="https://fonts.googleapis.com/css2?family=Source+Sans+3:wght@400;600&display=swap" rel="stylesheet">
<style>
  :root {
    --bg: #ffffff;
    --ink: #1d1d1b;
    --rose: #cf4f8e;
    --magenta-box: #c8468a;
    --gold-light: #f3e6c8;
    --gold: #c9a77a;
    --meadow-light: #e9f3d6;
    --meadow: #8fbf4a;
    --meadow-deep: #5f9a2a;
    --photo-tone: #3b4658;
  }
  * { margin: 0; padding: 0; box-sizing: border-box; }
  html, body { width: 880px; height: 1200px; overflow: hidden; background: var(--bg); }
  body { font-family: "Source Sans 3", "Segoe UI", sans-serif; color: var(--ink); }

  .back-cover { position: relative; width: 880px; height: 1200px; overflow: hidden; background: var(--bg); }

  .meadow {
    position: absolute; left: 0; right: 0; bottom: 0; height: 330px;
    background: linear-gradient(180deg, rgba(255,255,255,0) 0%, var(--meadow-light) 30%, var(--meadow) 62%, var(--meadow-deep) 100%);
  }

  .emblem {
    position: absolute; left: 331px; top: 34px; width: 220px; height: 220px; border-radius: 50%;
    background: radial-gradient(circle, #fffaf0 0%, var(--gold-light) 45%, rgba(255,255,255,0) 72%);
    border: 1.5px solid var(--gold);
  }

  .headline {
    position: absolute; top: 286px; left: 60px; right: 60px;
    text-align: center; color: var(--rose); font-weight: 600;
    font-size: 21px; line-height: 24px; letter-spacing: 0.2px; text-transform: uppercase;
  }

  .blurb {
    position: absolute; top: 367px; left: 92px; width: 696px;
    text-align: center; font-size: 17.5px; line-height: 23.7px;
  }
  .blurb p + p { margin-top: 24px; }

  .author-panel {
    position: absolute; left: 83px; top: 804px; width: 720px; height: 260px;
    background: var(--magenta-box); display: flex;
  }
  .author-portrait {
    width: 213px; height: 100%;
    background: linear-gradient(180deg, var(--magenta-box) 0%, #b9617f 35%, var(--photo-tone) 100%);
  }
  .author-bio {
    flex: 1; padding: 24px 14px 0 24px; color: #fff;
    font-size: 16px; line-height: 21.8px;
  }
</style>
</head>
<body>
<main class="back-cover">
  <div class="meadow" role="img" aria-label="Prairie verte fleurie de petites fleurs blanches"></div>

  <div class="emblem" role="img" aria-label="Motif géométrique doré de la fleur de vie"></div>

  <h2 class="headline">Et si votre maladie n’était autre que l’appel de<br>votre âme à retrouver votre essence véritable ?</h2>

  <section class="blurb">
    <p>Cet ouvrage est une invitation à entreprendre l’alchimie en vous grâce à l’Amour.</p>
    <p>Un chemin de guérison est et reste plus que jamais possible. Empreinte de sagesse Divine, la spiritualité est décryptée avec simplicité en y associant une compréhension globale de l’être âme corps esprit dans un recouvrement intégratif de la guérison. Vous y découvrirez une mine d’informations utiles pour vous aider à transmuter votre plomb en or.</p>
    <p>Concentré d’outils tant Ancestraux que modernes allant de l’Alimentation Saine Vivante et Vibrante, la Respiration Consciente, l’Aromathérapie, l’EFT, l’Auto-hypnose Humaniste, la Lithothérapie, la Musicothérapie, la Réflexologie Plantaire… aux Médecines millénaires du monde sans oublier les possibilités offertes par les thérapies Quantiques dans une dimension énergétique multidimensionnelle de l’être.</p>
  </section>

  <section class="author-panel">
    <div class="author-portrait" role="img" aria-label="Portrait de l’auteur en veste sombre et chemise claire"></div>
    <p class="author-bio">LUCIEN MARVAUD, formé à la santé de l’Habitat avec le Feng Shui Traditionnel Chinois et la Géobiologie et différents outils de santé holistique allant de l’Aromathérapie aux Thérapies Quantiques.<br>L’écriture de ce livre lui est apparue comme un appel du cœur désireux d’apporter une aide significative pour prévenir et aider à traiter le cancer ou toutes autres maladies différemment sous un angle intégratif âme-corps-esprit sans rejeter la médecine conventionnelle, mais l’inclure dans une réalité plus vaste.</p>
  </section>
</main>
</body>
</html>
```